Criação de Papelaria Profissional para Beleza
" CLÍNICA DE ESTÉTICA COMPLETA, COM ÊNFASE EM ATENDIMENTO PRÊMIUM (salas exclusivas, máquinas próprias, ambiente aconchegante com forte conexão nordestina) Serviços ofertados: Estética corporal, facial, injetáveis e laser) SITE: https://brunelva.com.br/ "

```html
<!DOCTYPE html>
<html lang="pt-BR">
<head>
<meta charset="utf-8">
<title>Brunelva – Pasta Institucional</title>
<link rel="stylesheet" href="https://fonts.googleapis.com/css2?family=Cormorant+Garamond:wght@400;500&family=Montserrat:wght@300;400&display=swap">
<style>
  :root {
    --backdrop: #c3938c;
    --paper: #f3f0f0;
    --paper-shade: #e9e5e5;
    --rose: #c98a7f;
    --rose-soft: #d8aaa2;
  }
  * { margin: 0; padding: 0; box-sizing: border-box; }
  html, body { width: 1200px; height: 1200px; overflow: hidden; }
  body { background: var(--backdrop); position: relative; font-family: "Montserrat", sans-serif; }

  .folder { position: absolute; left: 80px; top: 220px; width: 1040px; height: 760px; display: flex; }
  .panel { position: relative; width: 520px; height: 760px; background: var(--paper); }
  .panel--back { background: var(--paper-shade); }

  .mark { width: 44px; height: 44px; border-radius: 50%; background: var(--rose); }
  .brand-name {
    font-family: "Cormorant Garamond", serif; font-weight: 500; color: var(--rose);
    letter-spacing: 0.28em; text-transform: uppercase; line-height: 1;
  }
  .brand-sub {
    font-family: "Montserrat", sans-serif; font-weight: 400; color: var(--rose);
    letter-spacing: 0.42em; text-transform: uppercase; line-height: 1;
  }

  /* back panel */
  .back-brand { position: absolute; left: 52px; top: 400px; display: flex; flex-direction: column; align-items: flex-start; }
  .back-brand .mark { width: 34px; height: 34px; margin-left: 22px; margin-bottom: 8px; }
  .back-brand .brand-name { font-size: 22px; }
  .back-brand .brand-sub { font-size: 6px; margin-top: 6px; }

  .contacts { position: absolute; left: 52px; top: 490px; list-style: none; }
  .contacts li { display: flex; align-items: flex-start; gap: 8px; font-size: 9px; color: var(--rose); line-height: 1.35; margin-bottom: 7px; }
  .contacts svg { width: 10px; height: 10px; flex: none; margin-top: 1px; }

  /* front panel */
  .front-brand { position: absolute; left: 0; right: 0; top: 440px; display: flex; flex-direction: column; align-items: center; }
  .front-brand .mark { width: 62px; height: 62px; margin-bottom: 14px; }
  .front-brand .brand-name { font-size: 46px; padding-left: 0.28em; }
  .front-brand .brand-sub { font-size: 10px; margin-top: 10px; padding-left: 0.42em; }
  .tagline {
    margin-top: 26px; font-size: 15px; font-weight: 300; color: var(--rose);
    text-align: center; line-height: 1.35;
  }
</style>
</head>
<body>
  <main class="folder">
    <section class="panel panel--back">
      <div class="back-brand">
        <div class="mark"></div>
        <span class="brand-name">Brunelva</span>
        <span class="brand-sub">Clínica de Estética</span>
      </div>
      <ul class="contacts">
        <li>
          <svg viewBox="0 0 10 10"><path d="M2 1l2 2-1 1.2a6 6 0 0 0 2.8 2.8L7 6l2 2-1.3 1.3C4.5 9 1 5.5.7 2.3z" fill="var(--rose)"/></svg>
          (81) 3000-0000
        </li>
        <li>
          <svg viewBox="0 0 10 10"><circle cx="5" cy="5" r="4.2" fill="none" stroke="var(--rose)" stroke-width="1"/></svg>
          @brunelvaclinica
        </li>
        <li>
          <svg viewBox="0 0 10 10"><rect x=".6" y="2" width="8.8" height="6" fill="none" stroke="var(--rose)" stroke-width="1"/><path d="M.6 2L5 5.5 9.4 2" fill="none" stroke="var(--rose)" stroke-width="1"/></svg>
          brunelva.com.br
        </li>
        <li>
          <svg viewBox="0 0 10 10"><path d="M5 9.6S1.8 6 1.8 3.8a3.2 3.2 0 0 1 6.4 0C8.2 6 5 9.6 5 9.6z" fill="var(--rose)"/><circle cx="5" cy="3.8" r="1.1" fill="var(--paper)"/></svg>
          <span>Rua das Flores, 120, Boa Viagem<br>Recife, PE 51020-000</span>
        </li>
      </ul>
    </section>

    <section class="panel panel--front">
      <div class="front-brand">
        <div class="mark"></div>
        <h1 class="brand-name">Brunelva</h1>
        <p class="brand-sub">Clínica de Estética</p>
        <p class="tagline">Cuidando e exaltando a beleza e<br>o bem-estar dos nordestinos.</p>
      </div>
    </section>
  </main>
</body>
</html>
```